Providing Back Office Solutions to Financial Advisors and Attorney Needs a Business Card Design

Need a Business Card Design that speaks to Financial Advisor and Attorneys. Some of the word that come to mind is Clean/Simple & Futuristic.

Industry/Entity Type

Business

```html
<!DOCTYPE html>
<html lang="en">
<head>
<meta charset="utf-8">
<title>Veridan Back Office Solutions — Business Card</title>
<link href="https://fonts.googleapis.com/css2?family=Open+Sans:ital,wght@0,400;0,700;1,400&display=swap" rel="stylesheet">
<style>
  :root {
    --stage: #7f7f7f;
    --card: #ffffff;
    --ink: #111111;
    --ink-soft: #2a2a2a;
    --brand: #1f5fbf;
    --brand-deep: #1a4fa8;
    --brand-light: #4f8fd6;
    --icon: #6b6b6b;
  }
  * { margin: 0; padding: 0; box-sizing: border-box; }
  html, body {
    width: 1200px; height: 1200px; overflow: hidden;
    background: var(--stage);
    font-family: "Open Sans", sans-serif;
  }
  .stage { position: relative; width: 1200px; height: 1200px; }
  .card {
    position: absolute; left: 170px; width: 860px; height: 510px;
    box-shadow: 0 10px 24px rgba(0,0,0,0.35);
    overflow: hidden;
  }
  .card-front { top: 40px; background: var(--card); }
  .card-back {
    top: 630px;
    background: linear-gradient(135deg, var(--brand-deep) 0%, var(--brand-light) 50%, var(--brand-deep) 100%);
  }
  .person-name {
    position: absolute; left: 48px; top: 44px;
    font-weight: 700; font-size: 43px; color: var(--ink); line-height: 1;
  }
  .person-title {
    position: absolute; left: 46px; top: 100px;
    font-style: italic; font-size: 25px; color: var(--brand); line-height: 1;
  }
  .brand {
    position: absolute; left: 46px; top: 236px;
    display: flex; align-items: center; gap: 16px;
    width: 380px;
  }
  .brand-square { width: 64px; height: 64px; background: var(--brand); flex: none; }
  .brand-text { display: flex; flex-direction: column; }
  .brand-name {
    font-weight: 400; font-size: 44px; color: var(--brand);
    line-height: 1; letter-spacing: 2px;
  }
  .brand-tagline {
    margin-top: 8px;
    font-weight: 400; font-size: 18px; color: var(--brand);
    line-height: 1; white-space: nowrap;
  }
  .contacts {
    position: absolute; left: 452px; top: 208px; list-style: none;
  }
  .contacts li {
    display: flex; align-items: center; gap: 16px;
    height: 33px; font-size: 24px; color: var(--ink-soft);
  }
  .contacts svg { width: 24px; height: 24px; flex: none; }
  .address {
    position: absolute; left: 0; right: 0; top: 423px;
    text-align: center; font-size: 22px; letter-spacing: 1.5px; color: var(--ink-soft);
  }
  .band {
    position: absolute; left: 0; right: 0; bottom: 0; height: 26px;
    background: linear-gradient(90deg, var(--brand-deep), var(--brand-light) 55%, var(--brand-deep));
  }
</style>
</head>
<body>
<main class="stage">
  <section class="card card-front" aria-label="Card front">
    <h1 class="person-name">Name Here</h1>
    <p class="person-title">Chief Executive Officer</p>

    <div class="brand">
      <span class="brand-square"></span>
      <div class="brand-text">
        <p class="brand-name">VERIDAN</p>
        <p class="brand-tagline">BACK OFFICE SOLUTIONS</p>
      </div>
    </div>

    <ul class="contacts">
      <li>
        <svg viewBox="0 0 24 24"><rect x="1" y="1" width="22" height="22" rx="3" fill="var(--icon)"/><rect x="8" y="4" width="8" height="16" rx="1.5" fill="#fff"/><rect x="9.5" y="6" width="5" height="10" fill="var(--icon)"/></svg>
        (000) 000-0000
      </li>
      <li>
        <svg viewBox="0 0 24 24"><rect x="1" y="1" width="22" height="22" rx="3" fill="var(--icon)"/><path d="M5 10c0-3 14-3 14 0v1h-4v-1.5h-6V11H5z" fill="#fff"/><rect x="6" y="12" width="12" height="7" rx="1.5" fill="#fff"/><circle cx="12" cy="15.5" r="2" fill="var(--icon)"/></svg>
        (000) 000-0000
      </li>
      <li>
        <svg viewBox="0 0 24 24"><rect x="1" y="1" width="22" height="22" rx="3" fill="var(--icon)"/><rect x="6" y="5" width="12" height="14" rx="1" fill="#fff"/><rect x="8" y="7" width="8" height="3" fill="var(--icon)"/><rect x="8" y="12" width="2" height="2" fill="var(--icon)"/><rect x="11" y="12" width="2" height="2" fill="var(--icon)"/><rect x="14" y="12" width="2" height="2" fill="var(--icon)"/><rect x="8" y="15" width="2" height="2" fill="var(--icon)"/><rect x="11" y="15" width="2" height="2" fill="var(--icon)"/><rect x="14" y="15" width="2" height="2" fill="var(--icon)"/></svg>
        (000) 000-0000
      </li>
      <li>
        <svg viewBox="0 0 24 24"><rect x="1" y="1" width="22" height="22" rx="3" fill="var(--icon)"/><rect x="5" y="7" width="14" height="10" fill="#fff"/><path d="M5 7l7 6 7-6" fill="none" stroke="var(--icon)" stroke-width="1.5"/></svg>
        name@email.com
      </li>
      <li>
        <svg viewBox="0 0 24 24"><rect x="1" y="1" width="22" height="22" rx="3" fill="var(--icon)"/><path d="M4 12l8-7 8 7h-2.5v7h-11v-7z" fill="#fff"/><rect x="10.5" y="14" width="3" height="5" fill="var(--icon)"/></svg>
        www.domain.com
      </li>
    </ul>

    <p class="address">Address, Street, City, State, Zip Code</p>
    <div class="band"></div>
  </section>

  <section class="card card-back" role="img" aria-label="Card back: repeating decorative pattern in blue tones"></section>
</main>
</body>
</html>
```